Company providing wellness products (skin care, herbal, soap) needs website design.

Our company name is Amber Heron Fields and we provide wellness products for our customers. We also provide organically grown vegetables and herbs. Our website is on Wix and we have the basic layout completed; however, we need a better design. I assume this means that we can import the designs that you provide into the Wix environment. If this is not true, we do not want to move forward with the project. I included a copy of a logo that was done by your team.

Target Market(s)

women with income exceeded 75k interested in health and natural products.

Industry/Entity Type

Skin Care Product

Number of Pages Required

5+ page

Font styles to use
Serif
Sans Serif
Decorative
Script

Requirements
Must have
• Not sure of the number of pages as I really need a theme designed that I can carry throughout the site.
Nice to have
• clean, fresh, organic sophisticated feel. I would like to incorporate our logo that I attached. We are open to a different logo if it works better with your design. Our name is Amber Heron Fields and our logo is green so I think green should be incorporated but are open to what you design.

```html
<!DOCTYPE html>
<html lang="en">
<head>
<meta charset="utf-8">
<title>Amber Heron Fields — Rooted in Nature</title>
<link rel="stylesheet" href="https://fonts.googleapis.com/css2?family=Poppins:wght@400;500;600;700&family=Allura&display=swap">
<style>
:root{
  --green:#7aa83f;
  --green-soft:#b5cf9e;
  --script:#a9c98a;
  --ink:#111111;
  --text:#333333;
  --hero-bg:#f2f2f3;
  --section-gray:#f0f0f1;
  --white:#ffffff;
}
*{margin:0;padding:0;box-sizing:border-box}
html,body{width:1200px;height:3056px;overflow:hidden;background:var(--white)}
body{position:relative;font-family:'Poppins',sans-serif;color:var(--text)}
.abs{position:absolute}
.topbar{left:0;top:0;width:1200px;height:75px;background:var(--green)}
.nav{top:28px;left:458px;display:flex;gap:37px;font-size:14px;color:var(--white)}
.cart{top:28px;left:944px;font-size:14px;color:var(--white);display:flex;align-items:center;gap:6px}
.brand-disc{left:115px;top:-98px;width:244px;height:244px;border-radius:50%;background:var(--white)}
.brand-name{left:115px;top:86px;width:244px;text-align:center;font-size:18px;font-weight:500;color:var(--green);line-height:1.1}
.brand-dot{left:225px;top:40px;width:24px;height:24px;border-radius:50%;background:var(--green)}
.hero-bg{left:0;top:75px;width:1200px;height:500px;background:var(--hero-bg)}
.hero-art{left:100px;top:130px;width:420px;height:380px;border-radius:50%;background:radial-gradient(circle,#e4e4e6,rgba(242,242,243,0))}
.hero-title{left:140px;top:256px;width:500px;text-align:center;font-size:50px;font-weight:700;color:var(--green)}
.hero-tag{left:140px;top:321px;width:500px;text-align:center;font-size:16px;letter-spacing:3px;color:var(--ink);font-weight:500}
.btn-solid{left:318px;top:371px;width:142px;height:41px;border-radius:21px;background:var(--green);color:var(--white);font-size:14px;display:flex;align-items:center;justify-content:center}
.hero-photo{left:598px;top:119px;width:408px;height:408px;border-radius:50%;border:7px solid var(--green);background:linear-gradient(135deg,#1f5f9a 0%,#c99a7c 45%,#e0b393 70%,#2f6b3a 100%)}
.script{font-family:'Allura',cursive;color:var(--script);text-align:center;width:1200px;left:0;line-height:1}
.section-title{left:0;width:1200px;text-align:center;font-weight:700;color:var(--ink)}
.about-text{left:197px;top:810px;width:806px;text-align:center;font-size:12.5px;line-height:22.5px;color:var(--text)}
.btn-outline{left:529px;top:932px;width:142px;height:42px;border-radius:21px;border:1.5px solid var(--green-soft);box-shadow:0 3px 6px rgba(0,0,0,.12);color:var(--green);font-size:14px;display:flex;align-items:center;justify-content:center;background:var(--white)}
.specials-band{left:0;top:1276px;width:1200px;height:256px;background:var(--green-soft)}
.special-card{background:var(--white);width:266px}
.special-card .photo{width:266px;height:192px}
.special-card .label{height:33px;padding-left:15px;display:flex;align-items:center;font-size:14px;color:var(--ink);background:#f4f4f4}
.arrow{width:20px;height:30px}
.product{width:191px}
.product .photo{width:191px;height:168px;position:relative}
.product .name{font-size:15px;color:var(--green);margin:10px 0 0 16px}
.product .price{font-size:11px;color:var(--ink);margin:0 0 0 16px}
.product.featured{box-shadow:0 6px 12px rgba(0,0,0,.12);height:228px}
.add-cart{position:absolute;left:41px;top:125px;width:109px;height:32px;border-radius:16px;background:var(--green);color:var(--white);font-size:11px;display:flex;align-items:center;justify-content:center}
.blog-bg{left:0;top:2055px;width:1200px;height:500px;background:var(--section-gray)}
.post{width:414px}
.post .photo{width:414px;height:231px}
.post h3{font-size:23.5px;font-weight:600;line-height:27px;color:var(--ink);margin:34px 0 0 6px}
.post .meta{font-size:12px;color:var(--ink);margin:12px 0 0 7px}
.foot-name{left:0;top:2838px;width:1200px;text-align:center;font-size:21px;font-weight:500;color:var(--green)}
.foot-nav{left:0;top:2891px;width:1200px;display:flex;justify-content:center;gap:36px;font-size:14px;color:var(--ink)}
.social{top:2947px;left:502px;display:flex;gap:34px}
.social span{width:24px;height:24px;border-radius:50%;border:2.5px solid var(--ink)}
.copy{left:0;top:2993px;width:1200px;text-align:center;font-size:13px;color:var(--ink)}
</style>
</head>
<body>
<div class="abs hero-bg"></div>
<div class="abs hero-art" role="img" aria-label="Soft faded still life of soap, towel and botanical sprigs"></div>
<svg class="abs" style="left:0;top:480px" width="1200" height="110" viewBox="0 0 1200 110">
  <path d="M0 0 L0 18 Q600 160 1200 18 L1200 110 L0 110 Z" fill="#fff"/>
  <path d="M0 18 Q600 160 1200 18" fill="none" stroke="#7aa83f" stroke-width="7"/>
</svg>
<header>
  <div class="abs topbar"></div>
  <div class="abs brand-disc"></div>
  <div class="abs brand-dot"></div>
  <div class="abs brand-name">Amber Heron Fields</div>
  <nav class="abs nav"><span>Home</span><span>About Us</span><span>Shop</span><span>Blog</span><span>Contact Us</span></nav>
  <div class="abs cart">
    <svg width="13" height="12" viewBox="0 0 13 12"><path d="M1 1h2l2 7h6l1-5H4" fill="none" stroke="#fff" stroke-width="1.2"/><circle cx="6" cy="10.5" r="1" fill="#fff"/><circle cx="10" cy="10.5" r="1" fill="#fff"/></svg>
    Cart : (0)
  </div>
</header>

<section class="hero">
  <div class="abs hero-title">Amber Heron</div>
  <div class="abs hero-tag">ROOTED IN NATURE</div>
  <div class="abs btn-solid">SHOP NOW</div>
  <div class="abs hero-photo" role="img" aria-label="Portrait of a woman with a yellow orchid and palm leaves"></div>
  <svg class="abs arrow" style="left:168px;top:281px" viewBox="0 0 20 30"><path d="M15 4 L5 15 L15 26" fill="none" stroke="#555" stroke-width="3"/></svg>
  <svg class="abs arrow" style="left:1010px;top:291px" viewBox="0 0 20 30"><path d="M5 4 L15 15 L5 26" fill="none" stroke="#555" stroke-width="3"/></svg>
</section>

<section class="about">
  <div class="abs script" style="top:680px;font-size:110px">Amber Heron</div>
  <h2 class="abs section-title" style="top:735px;font-size:47px">About Us</h2>
  <p class="abs about-text">Sed ut perspiciatis unde omnis iste natus error sit voluptatem accusantium doloremque laudantium, totam rem aperiam, eaque ipsa quae ab illo inventore veritatis et quasi architecto beatae vitae dicta sunt explicabo. Nemo enim ipsam voluptatem quia voluptas sit aspernatur aut odit aut fugit, sed quia consequuntur magni dolores eos qui ratione voluptatem sequi nesciunt. Neque porro quisquam est, qui dolorem ipsum quia dolor sit amet,</p>
  <div class="abs btn-outline">SHOP NOW</div>
</section>

<section class="specials">
  <div class="abs script" style="top:1025px;font-size:110px">Our Products</div>
  <h2 class="abs section-title" style="top:1078px;font-size:47px">Our Specials</h2>
  <div class="abs specials-band"></div>
  <div class="abs special-card" style="left:179px;top:1192px">
    <div class="photo" role="img" aria-label="Self care gift box with jars, bottles and natural packaging" style="background:linear-gradient(135deg,#c9a27a,#efe6da 55%,#8a6a48)"></div>
    <div class="label">ORGANIC WELLNESS PRODUCTS</div>
  </div>
  <div class="abs special-card" style="left:471px;top:1231px">
    <div class="photo" role="img" aria-label="Woman in a towel wearing a face mask holding a leaf" style="background:linear-gradient(135deg,#e6e6e8,#d8cfc8 60%,#cfcfd2)"></div>
    <div class="label">SKIN CARE PRODUCTS</div>
  </div>
  <div class="abs special-card" style="left:761px;top:1193px">
    <div class="photo" role="img" aria-label="Hands holding freshly picked tomatoes over garden greens" style="background:linear-gradient(135deg,#3b4a2c,#6d2a1a 50%,#2d3a22)"></div>
    <div class="label">VEGETABLES AND HERB</div>
  </div>
</section>

<section class="featured">
  <div class="abs script" style="top:1540px;font-size:110px">Shop</div>
  <h2 class="abs section-title" style="top:1606px;font-size:51px">Featured Products</h2>
  <svg class="abs arrow" style="left:180px;top:1625px" viewBox="0 0 20 30"><path d="M15 4 L5 15 L15 26" fill="none" stroke="#555" stroke-width="3"/></svg>
  <svg class="abs arrow" style="left:1006px;top:1625px" viewBox="0 0 20 30"><path d="M5 4 L15 15 L5 26" fill="none" stroke="#555" stroke-width="3"/></svg>
  <div class="abs product featured" style="left:176px;top:1717px">
    <div class="photo" role="img" aria-label="Cosmetic bottles on a wooden tray with cotton flowers" style="background:linear-gradient(135deg,#e9e9e9,#c4a27d 50%,#efefef)">
      <div class="add-cart">ADD TO CART</div>
    </div>
    <div class="name">Product Name</div>
    <div class="price">$567 / 50 ml</div>
  </div>
  <div class="abs product" style="left:395px;top:1717px">
    <div class="photo" role="img" aria-label="Hands holding a white cream bottle with small flowers" style="background:linear-gradient(135deg,#f3f3f3,#dedede 60%,#eef2ea)"></div>
    <div class="name">Product Name</div>
    <div class="price">$567 / 50 ml</div>
  </div>
  <div class="abs product" style="left:615px;top:1717px">
    <div class="photo" role="img" aria-label="Cream jar and pump bottle on a pink background with blossoms" style="background:linear-gradient(135deg,#f2a0a4,#f6d2d2 55%,#e58a90)"></div>
    <div class="name">Product Name</div>
    <div class="price">$567 / 50 ml</div>
  </div>
  <div class="abs product" style="left:835px;top:1717px">
    <div class="photo" role="img" aria-label="Soap bar, cream bowl and nuts with green leaves" style="background:linear-gradient(135deg,#f1f1f1,#e7d6b5 50%,#f3f3f3)"></div>
    <div class="name">Product Name</div>
    <div class="price">$567 / 50 ml</div>
  </div>
</section>

<section class="news">
  <div class="abs blog-bg"></div>
  <svg class="abs" style="left:0;top:2370px" width="1200" height="200" viewBox="0 0 1200 200">
    <path d="M0 14 Q600 260 1200 14 L1200 200 L0 200 Z" fill="#fff"/>
  </svg>
  <div class="abs script" style="top:2095px;font-size:110px">Blog</div>
  <h2 class="abs section-title" style="top:2160px;font-size:47px">Latest News</h2>
  <article class="abs post" style="left:174px;top:2271px">
    <div class="photo" role="img" aria-label="Handmade soap bars with wildflowers" style="background:linear-gradient(135deg,#6d7a4a,#d9a45a 45%,#f1d79a 65%,#8a5a8a)"></div>
    <h3>Quis autem vel eum iure reprehenderit qui in ea voluptate</h3>
    <div class="meta">By : Auther name &nbsp;&nbsp;|&nbsp;&nbsp; Jan 02-2021</div>
  </article>
  <article class="abs post" style="left:613px;top:2271px">
    <div class="photo" role="img" aria-label="Natural soap with lemon, oats, almonds and oil" style="background:linear-gradient(135deg,#e8d46a,#a7c4c0 45%,#c9b89a 70%,#7a5a3a)"></div>
    <h3>Quis autem vel eum iure reprehenderit qui in ea voluptate</h3>
    <div class="meta">By : Auther name &nbsp;&nbsp;|&nbsp;&nbsp; Jan 02-2021</div>
  </article>
</section>

<footer>
  <svg class="abs" style="left:0;top:2695px" width="1200" height="110" viewBox="0 0 1200 110">
    <path d="M0 98 Q600 -80 1200 98" fill="none" stroke="#7aa83f" stroke-width="9"/>
  </svg>
  <div class="abs" style="left:588px;top:2800px;width:24px;height:24px;border-radius:50%;background:var(--green)"></div>
  <div class="abs foot-name">Amber Heron Fields</div>
  <nav class="abs foot-nav"><span>Home</span><span>About Us</span><span>Shop</span><span>Blog</span><span>Contact Us</span></nav>
  <div class="abs social" aria-label="Social links"><span></span><span></span><span></span><span></span></div>
  <div class="abs copy">© 2021 &nbsp;|&nbsp;&nbsp; www.amberheronfields.com</div>
</footer>
</body>
</html>
```